International Manufacturing Business Needs A Heavy Hitting Wordpress Design!

We need wordpress template designs for a new website for our UK based International company Tolvane Engineering Ltd. We manufacture and supply steel security doors and window units. We would like designs that feature the black and yellow industrial "stripes" that can be seen at our current site www.tolvadoors.com. The final design should communicate strength, power and weight to represent the quality of the products and the security that they provide.

It feels like we need 3 different types of page to be able to be created as per the current website at www.tolvasecuredoors.com.

Homepage
Products/Accessories
Leadtimes/Downloads/Contact

It may be that 3 different page types can be created with one template. I'm totally open to this.

I don't like the way that the site currently handles product images, nobody wants to click on even thumbnail to see the product. http://tolvasecuredoors.com/products/personnel-doors/

Totally open to suggestions on layout to enable the feeling outlined in the brief above.

Please ask if anything is not clear or you need answers to drill down on specifics.

Sick

Target Market(s)

Businesses that buy steel doors

Font styles to use
Sans Serif
Other font styles liked:
• Copperplate Gothic Bold - For Company Name but we are open to suggestions

Colors

Designer to choose colors to be used in the design.

Requirements
Must have
• Professional looking, clean design
• Conveys strength, power and weight to represent the quality of the products, the characteristics of steel and the security that they provide.
• Incorporates black and yellow stripes of our branding
• Ability to create pages with content as seen at www.tolvasecuredoors.com
• A better way of showing the product images
Nice to have
• If possible. a design that gives off the feeling that not only do we supply the products we also make them in house too. I don't know what this looks like but a way of differentiating between a supply only business and one that manufacturers the product too.
Should not have
• We don't like the current thumbnail method of showing the product images

```html
<!DOCTYPE html>
<html lang="en">
<head>
<meta charset="utf-8">
<title>Tolvane Engineering Ltd</title>
<link href="https://fonts.googleapis.com/css2?family=Oswald:wght@400;600;700&family=Roboto:wght@300;400;500;700&display=swap" rel="stylesheet">
<style>
:root{
  --yellow:#f5c400;
  --yellow-dark:#d9ad00;
  --black:#141414;
  --ink:#222;
  --muted:#666;
  --line:#e2e2e2;
  --white:#fff;
  --steel-a:#2a2a2a;
  --steel-b:#4a4a4a;
  --hero-a:#2e1a10;
  --hero-b:#5b3a26;
  --stripes:repeating-linear-gradient(135deg,var(--yellow) 0 18px,var(--black) 18px 36px);
}
*{box-sizing:border-box;margin:0;padding:0}
html,body{width:1200px;height:2266px;overflow:hidden}
body{position:relative;font-family:"Roboto",Arial,sans-serif;color:var(--ink);background:var(--white)}
.abs{position:absolute}
.heading{font-family:"Oswald","Arial Narrow",sans-serif}

/* header */
.top-stripes{left:0;top:0;width:1200px;height:8px;background:var(--stripes)}
.brand{left:132px;top:28px;display:flex;align-items:center;gap:12px}
.brand-mark{width:40px;height:40px;background:var(--yellow)}
.brand-name{font-family:"Oswald","Arial Narrow",sans-serif;font-weight:700;font-size:22px;line-height:24px;color:var(--black);letter-spacing:.5px;text-transform:uppercase}
.contact-item{top:30px}
.contact-item .label{display:flex;align-items:center;gap:8px;color:var(--muted);font-size:11px;margin-bottom:6px}
.contact-item .value{font-size:13px;font-weight:500;color:var(--ink)}
.contact-divider{left:908px;top:30px;width:1px;height:42px;background:var(--line)}
.header-rule{left:132px;top:92px;width:936px;height:1px;background:var(--line)}
.nav{left:132px;top:110px;display:flex;gap:28px;font-size:11px;font-weight:500;text-transform:uppercase;color:var(--ink)}
.nav .active{color:var(--yellow-dark)}
.order-btn{left:940px;top:100px;width:128px;height:32px;border-radius:16px;background:var(--yellow);color:var(--black);font-size:10.5px;font-weight:700;display:flex;align-items:center;justify-content:center;text-transform:uppercase}

/* hero */
.hero{left:0;top:140px;width:1200px;height:480px;background:linear-gradient(90deg,var(--hero-a),var(--hero-b) 60%,#4a2c1c)}
.hero-door{left:752px;top:160px;width:364px;height:440px;background:linear-gradient(180deg,#6b3f24,#8a5433)}
.hero-eyebrow{left:143px;top:253px;font-size:11px;font-weight:500;color:var(--yellow);text-transform:uppercase}
.hero-title{left:143px;top:272px;width:440px;font-size:40px;line-height:47px;color:var(--white);font-weight:400}
.btn{background:var(--yellow);color:var(--black);font-size:10px;font-weight:700;text-transform:uppercase;display:flex;align-items:center;justify-content:center}
.hero-btn{left:147px;top:431px;width:122px;height:37px}
.slider-arrow{top:337px;width:26px;height:26px;border-radius:50%;background:rgba(255,255,255,.15)}
.hero-wave{left:0;top:540px}

/* what we do */
.section-title{font-size:19px;font-weight:700;text-transform:uppercase;color:var(--ink);letter-spacing:.5px}
.section-title span{color:var(--yellow-dark)}
.title-rule{width:24px;height:2px;background:var(--black)}
.what-title{left:152px;top:650px}
.what-rule{left:152px;top:684px}
.what-list{left:160px;top:696px;width:560px;list-style:none;font-size:11px;font-weight:400;line-height:24px;color:#555}
.what-list li{position:relative;padding-left:14px}
.what-list li::before{content:"";position:absolute;left:0;top:11px;width:4px;height:1px;background:#999}
.what-btn{left:151px;top:977px;width:104px;height:32px}
.what-visual{left:805px;top:630px;width:330px;height:390px;background:linear-gradient(135deg,#9a6a3e,#6e6e73 55%,#a97845)}

/* products */
.products{left:0;top:1060px;width:1200px;height:566px;background:linear-gradient(180deg,var(--steel-b),var(--steel-a))}
.band-stripes{left:0;width:1200px;height:10px;background:var(--stripes)}
.products-title{left:0;top:1100px;width:1200px;text-align:center;color:var(--white);font-size:18px;font-weight:700;text-transform:uppercase;letter-spacing:.5px}
.tile{display:flex;align-items:center;justify-content:center;text-align:center;font-family:"Oswald","Arial Narrow",sans-serif;font-weight:600;text-transform:uppercase;font-size:17px;line-height:22px;color:var(--white)}
.tile::after{content:"";position:absolute;inset:4px;border:1px solid rgba(255,255,255,.6)}
.tile-personal{left:139px;top:1159px;width:314px;height:419px;background:linear-gradient(180deg,#b8692e,#9c5422)}
.tile-acoustic{left:469px;top:1157px;width:293px;height:206px;background:linear-gradient(135deg,#6f3d2a,#a55a3a 60%,#7a2b2b)}
.tile-blank{left:778px;top:1157px;width:293px;height:206px;background:linear-gradient(180deg,#e7e7e4,#cfcac2);color:var(--ink);align-items:flex-start;justify-content:flex-end;padding:34px 50px 0 0}
.tile-vandal{left:469px;top:1377px;width:293px;height:204px;background:var(--white);color:var(--ink);justify-content:flex-start;padding-left:20px;text-align:left}
.tile-vandal::after,.tile-blank::after{border-color:rgba(0,0,0,.08)}
.vandal-shutter{left:132px;top:26px;width:150px;height:164px;background:linear-gradient(135deg,#6f7f8f,#c9d3dc);z-index:0}
.vandal-label{position:relative;z-index:1}
.tile-fire{left:778px;top:1377px;width:293px;height:204px;background:linear-gradient(135deg,#cfe58a,#b5d959);color:#3c3c3c}

/* featured */
.featured-title{left:0;top:1676px;width:1200px;text-align:center}
.featured-rule{left:588px;top:1708px}
.tabs{left:135px;top:1732px;width:168px;text-align:center;text-transform:uppercase}
.tab-arrow{display:block;margin:0 auto}
.tab{font-size:10.5px;color:#bbb;padding:13px 0}
.tab.current{font-size:15px;color:var(--ink);text-transform:uppercase;border-top:1px solid #eee;border-bottom:1px solid #eee}
.door{top:1753px;width:76px;height:188px}
.door-label{top:1954px;width:160px;text-align:center;font-size:10.5px;color:#555}

/* footer */
.footer{left:0;top:2032px;width:1200px;height:234px;background:var(--black)}
.footer-brand{top:2106px}
.footer-brand .brand-name{color:var(--yellow)}
.badge{top:2114px;width:70px;height:44px;background:var(--white)}
.fcontact-title{left:638px;top:2104px;font-size:11px;font-weight:700;color:var(--white);text-transform:uppercase}
.fcontact-text{left:638px;top:2128px;font-size:10.5px;line-height:18px;color:#ddd}
.fcontact-text .mail{text-decoration:underline}
.fcontact-btn{left:639px;top:2174px;width:99px;height:27px;border:1px solid #888;color:var(--white);font-size:10px;display:flex;align-items:center;justify-content:center;gap:8px}
.fphone{left:834px;top:2106px;font-size:22px;font-weight:700;color:var(--white)}
.social{left:962px;top:2148px;display:flex;gap:9px}
.social i{display:block;width:17px;height:17px;border-radius:50%;background:var(--yellow)}
.copyright{left:760px;top:2188px;width:300px;text-align:right;font-size:8.5px;line-height:17px;color:#ccc}
</style>
</head>
<body>

<header>
  <div class="abs top-stripes"></div>
  <div class="abs brand">
    <span class="brand-mark"></span>
    <span class="brand-name">Tolvane<br>Engineering Ltd.</span>
  </div>
  <div class="abs contact-item" style="left:778px">
    <div class="label">
      <svg width="14" height="10" viewBox="0 0 14 10"><path d="M1 6c3-5 9-5 12 0l-3 2-1.5-2h-3L4 8z" fill="#d9ad00"/></svg>Call Us Today
    </div>
    <div class="value">+44 (0)1632 960 300</div>
  </div>
  <div class="abs contact-divider"></div>
  <div class="abs contact-item" style="left:937px">
    <div class="label">
      <svg width="14" height="10" viewBox="0 0 14 10"><rect width="14" height="10" fill="#d9ad00"/><path d="M0 0l7 5 7-5" stroke="#fff" fill="none"/></svg>Email Us
    </div>
    <div class="value">sales@tolvadoors.com</div>
  </div>
  <div class="abs header-rule"></div>
  <nav class="abs nav">
    <span class="active">Home</span><span>Products ▾</span><span>Accessories ▾</span><span>Delivery &amp; Lead Times</span><span>Downloads</span><span>Contact</span>
  </nav>
  <div class="abs order-btn">Online Order Form</div>
</header>

<section>
  <div class="abs hero" role="img" aria-label="Warm interior with a wall lamp and a panelled timber door"></div>
  <div class="abs hero-door" role="img" aria-label="Panelled wooden door in a moulded frame"></div>
  <div class="abs hero-eyebrow">Words of Wisdom</div>
  <h1 class="abs hero-title heading">We Have the Best Windows and Doors in the Market.</h1>
  <div class="abs btn hero-btn">Read More</div>
  <svg class="abs slider-arrow" style="left:86px" viewBox="0 0 26 26"><path d="M15 8l-5 5 5 5" stroke="#fff" fill="none" stroke-width="1.5"/></svg>
  <svg class="abs slider-arrow" style="left:1096px" viewBox="0 0 26 26"><path d="M11 8l5 5-5 5" stroke="#fff" fill="none" stroke-width="1.5"/></svg>
  <svg class="abs hero-wave" width="1200" height="82" viewBox="0 0 1200 82">
    <path d="M0 70 C300 10 700 0 1200 45 L1200 82 L0 82Z" fill="#f5c400"/>
    <path d="M0 82 C300 28 700 18 1200 64 L1200 82Z" fill="#fff"/>
  </svg>
</section>

<section>
  <h2 class="abs section-title heading what-title">What <span>We Do</span></h2>
  <div class="abs title-rule what-rule"></div>
  <ul class="abs what-list">
    <li>Tolvane security doors combine a high level of security with exceptional value.</li>
    <li>Our superior quality and proven reliability has made us the first choice for a wide range of companies no matter what their requirement or application.</li>
    <li>All of our products are designed and manufactured to the highest specification, combine this with a rigorous quality control system and an extensive after-sales service and it is easy to see why we are seen as industry leaders.</li>
    <li>We place particular emphasis on continuous development and twelve years experience ensures that we are always ahead of the competition and that we can react quickly to customer's requirements.</li>
    <li>Each and every Tolvane product is subject to our fifty point quality control process before it is dis-patched.</li>
    <li>Tolvane have forged a reputation for affordable, high quality steel doors.</li>
  </ul>
  <div class="abs btn what-btn">Read More</div>
  <div class="abs what-visual" role="img" aria-label="Exploded view of a steel security door showing frame, core and timber facing layers"></div>
</section>

<section>
  <div class="abs products" role="img" aria-label="Dimmed interior room in greyscale"></div>
  <div class="abs band-stripes" style="top:1060px"></div>
  <h2 class="abs products-title heading">Our Products</h2>
  <div class="abs tile tile-personal" role="img" aria-label="Timber-finish steel personnel door">Personal Doors</div>
  <div class="abs tile tile-acoustic" role="img" aria-label="Acoustic doors in a studio room">Acoustic<br>Doors</div>
  <div class="abs tile tile-blank" role="img" aria-label="Blank glazed door against a white wall">Blank<br>Doors</div>
  <div class="abs tile tile-vandal">
    <span class="vandal-label">Anti Vandal<br>Shutters</span>
    <div class="abs vandal-shutter" role="img" aria-label="Open steel anti vandal window shutter"></div>
  </div>
  <div class="abs tile tile-fire" role="img" aria-label="Orange fire exit door under green tint">Fire Exit Doors</div>
</section>

<section>
  <h2 class="abs section-title heading featured-title">Featured <span>Products</span></h2>
  <div class="abs title-rule featured-rule"></div>
  <div class="abs tabs">
    <svg class="tab-arrow" width="20" height="10" viewBox="0 0 20 10"><path d="M1 9l9-8 9 8" stroke="#ccc" fill="none"/></svg>
    <div class="tab">Interior Doors</div>
    <div class="tab current">Interior Doors</div>
    <div class="tab">Exterior Doors</div>
    <svg class="tab-arrow" width="20" height="10" viewBox="0 0 20 10"><path d="M1 1l9 8 9-8" stroke="#ccc" fill="none"/></svg>
  </div>
  <div class="abs door" style="left:370px;background:linear-gradient(180deg,#d9b483,#c79a63)" role="img" aria-label="Knotty pine panelled interior door"></div>
  <div class="abs door" style="left:537px;background:linear-gradient(180deg,#b66a3e,#9d5830)" role="img" aria-label="Oak panelled interior door"></div>
  <div class="abs door" style="left:687px;background:linear-gradient(180deg,#cbb8a6,#b29b86)" role="img" aria-label="Vertical boarded timber door"></div>
  <div class="abs door" style="left:828px;background:linear-gradient(180deg,#f4f4f4,#e2e2e2)" role="img" aria-label="White primed panel door"></div>
  <div class="abs door" style="left:982px;background:linear-gradient(180deg,#d99a60,#c4844a)" role="img" aria-label="Glazed timber door with small lites"></div>
  <div class="abs door-label" style="left:328px">Internal Norfield</div>
  <div class="abs door-label" style="left:495px">Internal Norfield</div>
  <div class="abs door-label" style="left:645px">Builders Stockline</div>
  <div class="abs door-label" style="left:786px">Internal Norfield</div>
  <div class="abs door-label" style="left:940px">Builders Stockline</div>
</section>

<footer>
  <div class="abs footer" role="img" aria-label="Dark interior doorway background"></div>
  <div class="abs band-stripes" style="top:2032px"></div>
  <div class="abs brand footer-brand">
    <span class="brand-mark"></span>
    <span class="brand-name">Tolvane<br>Engineering Ltd.</span>
  </div>
  <div class="abs badge" style="left:408px"></div>
  <div class="abs badge" style="left:499px"></div>
  <div class="abs fcontact-title">Contact Details</div>
  <div class="abs fcontact-text">E-Mail address<br><span class="mail">contact@tolvane.com</span></div>
  <div class="abs fcontact-btn">Contact us!
    <svg width="10" height="10" viewBox="0 0 10 10"><path d="M1 5l8-4-3 8-1-3z" stroke="#fff" fill="none"/></svg>
  </div>
  <div class="abs fphone heading">( +123 ) 456 789 000</div>
  <div class="abs social"><i></i><i></i><i></i><i></i></div>
  <div class="abs copyright">Copyright 1995 - 2018, tolvaneengineeringltd.com<br>All Rights Reserved</div>
</footer>

</body>
</html>
```